Looking for a cool & simple business-card-design for digital agency

Hi!

We are a web agency that offers Reputation Management, Zorvik & Seo Services and software development. We like cool things, we like innovative styles.

We have uploaded our logo.

Project Deadline Extended Reason: Client does not want any designs with the colorful logo. Please send us submissions ONLY with the blac and white logo. What the client would like to see:1) Back of the card: is a silver logo on a black background2) front of the card with all the data, please use white background and black logo thank you Added Friday, May 8, 2015

Software

```html
<!DOCTYPE html>
<html lang="en">
<head>
<meta charset="utf-8">
<title>Nettavia AG – Business Card</title>
<link rel="stylesheet" href="https://fonts.googleapis.com/css2?family=Arimo:wght@400&family=Josefin+Sans:wght@300;600;700&display=swap">
<style>
  :root {
    --card-bg: #ffffff;
    --ink: #000000;
    --ink-soft: #222222;
    --band-start: #0b7034;
    --band-mid: #5f9a3a;
    --band-end: #a9c33f;
    --band-text: #ffffff;
    --accent: #e4007d;
  }
  html, body {
    margin: 0;
    padding: 0;
    width: 1200px;
    height: 769px;
    overflow: hidden;
    background: var(--card-bg);
  }
  .card {
    position: relative;
    width: 1200px;
    height: 769px;
    background: var(--card-bg);
    overflow: hidden;
  }
  .brand {
    position: absolute;
    left: 48px;
    top: 46px;
    display: flex;
    align-items: center;
    gap: 18px;
  }
  .brand__square {
    width: 56px;
    height: 56px;
    background: var(--ink);
  }
  .brand__name {
    font-family: "Josefin Sans", sans-serif;
    font-weight: 700;
    font-size: 52px;
    line-height: 1;
    color: var(--ink);
    padding-top: 6px;
  }
  .person {
    position: absolute;
    left: 183px;
    top: 226px;
    width: 285px;
    text-align: center;
  }
  .person__name {
    font-family: "Josefin Sans", sans-serif;
    font-weight: 600;
    font-size: 50px;
    line-height: 1;
    color: var(--ink);
    margin: 0;
  }
  .person__role {
    font-family: "Josefin Sans", sans-serif;
    font-weight: 300;
    font-size: 29px;
    line-height: 1;
    color: var(--ink-soft);
    margin: 10px 0 0;
  }
  .contact {
    position: absolute;
    top: 448px;
    font-family: "Arimo", Arial, sans-serif;
    font-size: 34px;
    line-height: 46px;
    color: var(--ink);
    margin: 0;
  }
  .contact--address { left: 54px; }
  .contact--phones { left: 501px; }
  .contact__label {
    display: inline-block;
    width: 134px;
  }
  .band {
    position: absolute;
    left: 0;
    top: 600px;
    width: 896px;
    height: 130px;
  }
  .band__url {
    position: absolute;
    left: 0;
    top: 600px;
    width: 900px;
    height: 130px;
    display: flex;
    align-items: center;
    justify-content: center;
    font-family: "Arimo", Arial, sans-serif;
    font-size: 40px;
    color: var(--band-text);
  }
  .mark-corner {
    position: absolute;
    left: 915px;
    top: 600px;
    width: 240px;
    height: 130px;
    display: flex;
    align-items: center;
    justify-content: center;
    font-family: "Josefin Sans", sans-serif;
    font-weight: 700;
    font-size: 46px;
    color: var(--accent);
  }
</style>
</head>
<body>
  <main class="card">
    <header class="brand">
      <div class="brand__square"></div>
      <div class="brand__name">Nettavia AG</div>
    </header>

    <section class="person">
      <h1 class="person__name">MYNAME</h1>
      <p class="person__role">MYGREATPOSITION</p>
    </section>

    <p class="contact contact--address">
      MyStreet99<br>
      00000 MyCity<br>
      MyState, MyCountry
    </p>

    <p class="contact contact--phones">
      <span class="contact__label">Phone:</span>+ 01010101<br>
      <span class="contact__label">Fax:</span>+ 10101010<br>
      <span class="contact__label">Mobile:</span>+ 01010101
    </p>

    <svg class="band" viewBox="0 0 896 130" aria-hidden="true">
      <defs>
        <linearGradient id="bandGradient" x1="0" y1="0" x2="1" y2="0">
          <stop offset="0" stop-color="var(--band-start)"/>
          <stop offset="0.5" stop-color="var(--band-mid)"/>
          <stop offset="1" stop-color="var(--band-end)"/>
        </linearGradient>
      </defs>
      <polygon points="0,0 848,0 896,130 0,130" fill="url(#bandGradient)"/>
    </svg>
    <div class="band__url">www.nettavia-web.com</div>

    <div class="mark-corner">Nettavia</div>
  </main>
</body>
</html>
```